BrushGuard Tolland- Making Helena A Wildfire Adapted Community

Design a two complimentary graphics with text that can be used for a banner and "mini-billboard" to promote the project and encourage citizens to go to the webpage to learn more. Using the attached document as examples of what we want the two banners to say.
The goal of BrushGuard Tolland is to plan and prepare so if an urban wildfire occurs, catastrophic loss can be avoided. BrushGuard Tolland focuses on reducing the risk of and catastrophic losses to resources and private property on private land in Helena, MT. Property owners are encouraged to be proactive to address hazardous fuel conditions on their property, reduce structure ignition potential within their home ignition zone and employ wildfire resilient principles to sustain a fire adapted home, property and community. Ember showers from a wildfire next to the city is the biggest concern.

Target Market(s)

Residents in the project area of Helena. Signs and banners will be displayed on public lands and private yeards

Font styles to use
Sans Serif

Requirements
Must have
• Graphics, use of the MeadowlineBlaze Watch Planning Circle logo. Must incorporate the text that is part of the attachment.
Nice to have
• Get people's attention. A simple graphic that get's people's attention.
Should not have
• small details.

```html
<!DOCTYPE html>
<html lang="en">
<head>
<meta charset="utf-8">
<title>BrushGuard Tolland – Prepare Now Banner</title>
<link href="https://fonts.googleapis.com/css2?family=Archivo:wght@700;800;900&display=swap" rel="stylesheet">
<style>
  :root {
    --white: #ffffff;
    --leaf-green: #3cc41e;
    --alert-red: #d21a0c;
    --band-green: #00c81a;
    --band-edge: #72f41c;
    --prepare-yellow: #e4f81c;
    --choice-orange: #f36a17;
    --url-amber: #f5a524;
    --flame-red: #f0302a;
    --flame-orange: #ff6a1c;
    --ground-green: #3cc41e;
  }
  html, body {
    margin: 0;
    padding: 0;
    overflow: hidden;
    background: var(--white);
  }
  .banner {
    position: relative;
    width: 1200px;
    height: 402px;
    overflow: hidden;
    background: var(--white);
    font-family: "Archivo", Arial, Helvetica, sans-serif;
  }
  .banner__wave {
    position: absolute;
    inset: 0;
    width: 1200px;
    height: 402px;
  }
  .warning {
    position: absolute;
    left: 131px;
    top: 100px;
    transform: translateX(-50%);
    margin: 0;
    text-align: center;
    font-weight: 800;
    font-size: 27px;
    line-height: 32px;
    white-space: nowrap;
  }
  .warning__line { display: block; }
  .warning__line--green { color: var(--leaf-green); font-weight: 700; }
  .warning__line--red { color: var(--alert-red); font-weight: 900; }
  .hero-illustration {
    position: absolute;
    left: 306px;
    top: 58px;
    width: 196px;
    height: 254px;
    border-radius: 50% 50% 48% 48% / 62% 62% 38% 38%;
    background: radial-gradient(ellipse at 50% 70%, var(--flame-red) 0%, var(--flame-red) 45%, var(--flame-orange) 100%);
  }
  .hero-ground {
    position: absolute;
    left: 306px;
    top: 312px;
    width: 196px;
    height: 10px;
    border-radius: 50% 50% 0 0 / 100% 100% 0 0;
    background: var(--ground-green);
  }
  .callout {
    position: absolute;
    left: 953px;
    top: 105px;
    transform: translateX(-50%);
    margin: 0;
    text-align: center;
    font-weight: 900;
    font-size: 37px;
    line-height: 41px;
    letter-spacing: -0.3px;
    white-space: nowrap;
  }
  .callout__line { display: block; }
  .callout__line--prepare { color: var(--prepare-yellow); }
  .callout__line--home, .callout__line--loss { color: var(--white); }
  .callout__line--choice { color: var(--choice-orange); }
  .learn-more {
    position: absolute;
    left: 947px;
    top: 324px;
    transform: translateX(-50%);
    margin: 0;
    text-align: center;
    white-space: nowrap;
  }
  .learn-more__lead {
    display: block;
    color: var(--white);
    font-weight: 700;
    font-size: 19px;
    line-height: 26px;
  }
  .learn-more__url {
    display: block;
    color: var(--url-amber);
    font-weight: 800;
    font-size: 18px;
    line-height: 26px;
    letter-spacing: 2.6px;
  }
</style>
</head>
<body>
  <main class="banner">
    <svg class="banner__wave" viewBox="0 0 1200 402" aria-hidden="true">
      <path fill="var(--band-edge)" d="M878,0 C752,4 718,140 652,246 C590,346 500,398 296,402 L1200,402 L1200,0 Z"/>
      <path fill="var(--band-green)" d="M896,0 C776,6 746,146 684,250 C622,352 530,400 330,402 L1200,402 L1200,0 Z"/>
    </svg>

    <p class="warning">
      <span class="warning__line warning__line--green">You</span>
      <span class="warning__line warning__line--red">DO NOT</span>
      <span class="warning__line warning__line--green">Have to</span>
      <span class="warning__line warning__line--red">LIVE IN</span>
      <span class="warning__line warning__line--red">A FOREST</span>
      <span class="warning__line warning__line--green">to be in a</span>
      <span class="warning__line warning__line--red">WILDFIRE!</span>
    </p>

    <div class="hero-illustration" role="img" aria-label="Illustration of a house and evergreen trees engulfed in a large red and orange flame"></div>
    <div class="hero-ground" aria-hidden="true"></div>

    <h1 class="callout">
      <span class="callout__line callout__line--prepare">PREPARE NOW!</span>
      <span class="callout__line callout__line--home">Your home...</span>
      <span class="callout__line callout__line--loss">Your loss...</span>
      <span class="callout__line callout__line--choice">YOUR CHOICE!</span>
    </h1>

    <p class="learn-more">
      <span class="learn-more__lead">Learn more at BrushGuard Tolland</span>
      <span class="learn-more__url">WWW.MBWPC.ORG</span>
    </p>
  </main>
</body>
</html>
```